We are a family based professional house keeping and cleaning services company. we offer 30% off for the first cleaning to any new costumer with this post cards, we offer the best service in town 100% guaranteed or money backsome of the services we offer includemove in/out cleaningdeep cleaning in every visitsteam cleaningspecial event cleaningpersonalized cleaning to cover every costumer needs and any requestcontact info phone 513-630-6275email tidyhomesquad42@maplenest.com
Target Market(s)
middle and upper class
Industry/Entity Type
It Company
Colors
Designer to choose colors to be used in the design.
Look and feel

```html
<!DOCTYPE html>
<html lang="en">
<head>
<meta charset="utf-8">
<title>Cleaning Services Postcard</title>
<link rel="stylesheet" href="https://fonts.googleapis.com/css2?family=Mulish:wght@400;500;600;700;800;900&display=swap">
<style>
  :root {
    --brand-blue: #2fa3d9;
    --sky-blue: #7dcdf3;
    --navy: #25397a;
    --tick-blue: #2d82c4;
    --ink: #1f1f1f;
    --white: #ffffff;
    --cart-blue: #2a63c9;
    --cart-yellow: #f2cf1c;
    --cart-green: #4cc94f;
    --uniform-beige: #bfae8f;
    --uniform-light: #e4dac6;
  }
  * { margin: 0; padding: 0; box-sizing: border-box; }
  html, body { width: 1200px; height: 924px; overflow: hidden; background: var(--white); }
  .postcard {
    position: relative;
    width: 1200px;
    height: 924px;
    background: var(--white);
    overflow: hidden;
    font-family: "Mulish", "Nunito Sans", sans-serif;
    color: var(--ink);
  }
  .corner-wedge { position: absolute; right: 0; bottom: 0; width: 380px; height: 334px; }

  .cart-photo {
    position: absolute;
    left: 582px;
    top: 86px;
    width: 382px;
    height: 608px;
    border-radius: 40px;
    background:
      radial-gradient(ellipse 40% 22% at 45% 78%, rgba(242,207,28,0.85) 0%, rgba(242,207,28,0) 100%),
      radial-gradient(ellipse 30% 16% at 86% 86%, rgba(76,201,79,0.8) 0%, rgba(76,201,79,0) 100%),
      linear-gradient(180deg, rgba(47,163,217,0.35) 0%, rgba(42,99,201,0.55) 55%, rgba(42,99,201,0.75) 100%);
    opacity: 0.9;
  }
  .housekeeper-photo {
    position: absolute;
    left: 966px;
    top: 76px;
    width: 160px;
    height: 620px;
    border-radius: 60px 60px 30px 30px;
    background: linear-gradient(180deg, var(--uniform-light) 0%, var(--uniform-beige) 30%, var(--uniform-light) 48%, var(--uniform-beige) 70%, #a99a7e 100%);
    opacity: 0.85;
  }

  .title-panel {
    position: absolute;
    left: 0;
    top: 0;
    width: 598px;
    height: 486px;
    background: var(--brand-blue);
    color: var(--white);
    text-align: center;
  }
  .title-kicker {
    position: absolute;
    left: 0; right: 0; top: 56px;
    font-size: 44px;
    font-weight: 700;
    line-height: 44px;
    letter-spacing: 0.5px;
  }
  .title-rule {
    position: absolute;
    left: 58px;
    width: 490px;
    height: 2px;
    background: var(--white);
  }
  .title-rule.upper { top: 167px; }
  .title-rule.lower { top: 392px; }
  .title-main {
    position: absolute;
    left: 0; right: 0; top: 184px;
    font-size: 100px;
    font-weight: 900;
    line-height: 88px;
    letter-spacing: 1px;
  }
  .title-tagline {
    position: absolute;
    left: 0; right: 0; top: 416px;
    font-size: 27px;
    font-weight: 700;
    letter-spacing: 0.3px;
  }

  .service-list {
    position: absolute;
    left: 34px;
    top: 516px;
    list-style: none;
    font-size: 30px;
    font-weight: 500;
    line-height: 36.5px;
  }
  .service-list li { position: relative; padding-left: 40px; }
  .service-list .tick { position: absolute; left: 0; top: 10px; width: 28px; height: 22px; }

  .contact { position: absolute; left: 52px; top: 776px; font-style: normal; }
  .contact-phone {
    font-size: 60px;
    font-weight: 700;
    line-height: 70px;
    color: var(--navy);
  }
  .contact-phone .label { color: var(--brand-blue); }
  .contact-email {
    font-size: 25px;
    font-weight: 600;
    color: var(--brand-blue);
    line-height: 30px;
  }
</style>
</head>
<body>
<main class="postcard">
  <svg class="corner-wedge" viewBox="0 0 380 334" aria-hidden="true">
    <polygon points="0,334 380,334 380,0" fill="var(--sky-blue)"/>
  </svg>

  <div class="cart-photo" role="img" aria-label="Blue janitorial cart with brooms, mop, yellow and green buckets and spray bottles"></div>
  <div class="housekeeper-photo" role="img" aria-label="Housekeeper in a beige uniform and white apron holding a mop"></div>

  <section class="title-panel">
    <p class="title-kicker">A COMPLETE<br>PROFESSIONAL</p>
    <div class="title-rule upper"></div>
    <h1 class="title-main">CLEANING<br>SERVICES</h1>
    <div class="title-rule lower"></div>
    <p class="title-tagline">FOR ALL YOUR CLEANING NEEDS</p>
  </section>

  <ul class="service-list">
    <li><svg class="tick" viewBox="0 0 28 22" aria-hidden="true"><path d="M2 11 L10 19 L26 3" fill="none" stroke="var(--tick-blue)" stroke-width="4" stroke-linecap="round" stroke-linejoin="round"/></svg>we offer include move in/out cleaning</li>
    <li><svg class="tick" viewBox="0 0 28 22" aria-hidden="true"><path d="M2 11 L10 19 L26 3" fill="none" stroke="var(--tick-blue)" stroke-width="4" stroke-linecap="round" stroke-linejoin="round"/></svg>Deep cleaning in every visitsteam</li>
    <li><svg class="tick" viewBox="0 0 28 22" aria-hidden="true"><path d="M2 11 L10 19 L26 3" fill="none" stroke="var(--tick-blue)" stroke-width="4" stroke-linecap="round" stroke-linejoin="round"/></svg>Cleaning special event</li>
    <li><svg class="tick" viewBox="0 0 28 22" aria-hidden="true"><path d="M2 11 L10 19 L26 3" fill="none" stroke="var(--tick-blue)" stroke-width="4" stroke-linecap="round" stroke-linejoin="round"/></svg>Personalized cleaning</li>
    <li><svg class="tick" viewBox="0 0 28 22" aria-hidden="true"><path d="M2 11 L10 19 L26 3" fill="none" stroke="var(--tick-blue)" stroke-width="4" stroke-linecap="round" stroke-linejoin="round"/></svg>Cleaning to cover every costumer<br>needs and any request</li>
  </ul>

  <address class="contact">
    <p class="contact-phone"><span class="label">Call : </span>413-582-9174</p>
    <p class="contact-email">tidyhomesquad42@maplenest.com</p>
  </address>
</main>
</body>
</html>
```